Bref créative
Business Stationery
Velmora Vantage
Professional
Belinda Hawthorpe
Managing Director
Accra - Cork - Leeds
bel@velmoravantage.com
www.velmoravantage.com
Quorn Logo
logo vector file

```html
<!DOCTYPE html>
<html lang="en">
<head>
<meta charset="utf-8">
<title>Velmora Vantage — Business Cards</title>
<link rel="stylesheet" href="https://fonts.googleapis.com/css2?family=Open+Sans:wght@400;600;700&display=swap">
<style>
  :root {
    --page-bg: #eef0ef;
    --card-bg: #ffffff;
    --green-deep: #2f8a1f;
    --green-mid: #4fae2c;
    --green-light: #9fd46a;
    --ink: #4a4a4a;
    --ink-soft: #8a8a8a;
    --watermark: #e6ebe4;
  }
  * { box-sizing: border-box; margin: 0; padding: 0; }
  html, body { width: 1200px; height: 971px; overflow: hidden; }
  body {
    background: var(--page-bg);
    font-family: "Open Sans", Arial, sans-serif;
    position: relative;
  }
  .card {
    position: absolute;
    top: 330px;
    width: 520px;
    height: 310px;
    background: var(--card-bg);
    border-radius: 22px;
    overflow: hidden;
    box-shadow: 0 6px 18px rgba(0,0,0,0.12);
  }
  .card--front { left: 50px; }
  .card--back { left: 630px; }

  .front-wave { position: absolute; left: 0; bottom: 0; width: 520px; height: 310px; }

  .brand {
    position: absolute; left: 36px; top: 44px;
    display: flex; align-items: center; gap: 12px;
  }
  .brand__dot {
    width: 28px; height: 28px; border-radius: 50%;
    background: var(--green-mid);
  }
  .brand__name {
    font-weight: 700; font-size: 28px; line-height: 34px; color: var(--ink);
    letter-spacing: -0.5px; white-space: nowrap;
  }

  .contact-list {
    position: absolute; left: 38px; top: 102px;
    list-style: none;
  }
  .contact-list li {
    display: flex; align-items: center; gap: 7px;
    font-size: 10.5px; line-height: 16px; color: var(--ink);
    white-space: nowrap;
  }
  .contact-list svg { width: 11px; height: 11px; flex: none; }

  .person {
    position: absolute; right: 30px; bottom: 24px;
    text-align: right; color: #fff;
  }
  .person__name { font-weight: 600; font-size: 13px; line-height: 18px; }
  .person__role { font-size: 11px; line-height: 16px; opacity: 0.9; }

  .back-web {
    position: absolute; left: 0; right: 0; top: 78px;
    text-align: center; font-size: 12px; letter-spacing: 4px;
    color: var(--ink-soft); white-space: nowrap;
  }
  .back-mark {
    position: absolute; right: 60px; top: 120px;
    width: 150px; height: 150px; border-radius: 50%;
    background: var(--watermark);
  }
</style>
</head>
<body>
  <section class="card card--front" aria-label="Business card front">
    <svg class="front-wave" viewBox="0 0 520 310" aria-hidden="true">
      <defs>
        <linearGradient id="waveGreen" x1="0" y1="0" x2="1" y2="1">
          <stop offset="0" stop-color="#9fd46a"/>
          <stop offset="0.45" stop-color="#4fae2c"/>
          <stop offset="1" stop-color="#2f8a1f"/>
        </linearGradient>
      </defs>
      <path d="M0 200 C 120 170, 220 280, 340 250 C 420 230, 470 205, 520 210 L520 310 L0 310 Z" fill="#9fd46a" opacity="0.55"/>
      <path d="M0 215 C 130 190, 230 295, 350 262 C 430 240, 480 220, 520 225 L520 310 L0 310 Z" fill="url(#waveGreen)"/>
    </svg>

    <div class="brand">
      <span class="brand__dot"></span>
      <span class="brand__name">Velmora Vantage</span>
    </div>

    <ul class="contact-list">
      <li><svg viewBox="0 0 12 12"><circle cx="6" cy="6" r="6" fill="#4fae2c"/><path d="M6 2.6a2.2 2.2 0 0 0-2.2 2.2C3.8 6.6 6 9.4 6 9.4s2.2-2.8 2.2-4.6A2.2 2.2 0 0 0 6 2.6z" fill="#fff"/></svg>Accra - Cork - Leeds</li>
      <li><svg viewBox="0 0 12 12"><circle cx="6" cy="6" r="6" fill="#4fae2c"/><path d="M4 3h1.3l.6 1.6-.8.6a4 4 0 0 0 1.7 1.7l.6-.8L9 6.7V8a1 1 0 0 1-1 1A5 5 0 0 1 3 4a1 1 0 0 1 1-1z" fill="#fff"/></svg>00353 55 0142210</li>
      <li><svg viewBox="0 0 12 12"><circle cx="6" cy="6" r="6" fill="#4fae2c"/><path d="M4 3h1.3l.6 1.6-.8.6a4 4 0 0 0 1.7 1.7l.6-.8L9 6.7V8a1 1 0 0 1-1 1A5 5 0 0 1 3 4a1 1 0 0 1 1-1z" fill="#fff"/></svg>00234 555 0190347</li>
      <li><svg viewBox="0 0 12 12"><circle cx="6" cy="6" r="6" fill="#4fae2c"/><rect x="3" y="4" width="6" height="4.2" fill="#fff"/><path d="M3 4l3 2.3L9 4" stroke="#4fae2c" stroke-width="0.7" fill="none"/></svg>bel@velmoravantage.com</li>
      <li><svg viewBox="0 0 12 12"><circle cx="6" cy="6" r="6" fill="#4fae2c"/><circle cx="6" cy="6" r="3" fill="none" stroke="#fff" stroke-width="0.9"/><path d="M3 6h6M6 3v6" stroke="#fff" stroke-width="0.7"/></svg>www.velmoravantage.com</li>
    </ul>

    <div class="person">
      <p class="person__name">Belinda Hawthorpe</p>
      <p class="person__role">Managing Director</p>
    </div>
  </section>

  <section class="card card--back" aria-label="Business card back">
    <p class="back-web">www.velmoravantage.com</p>
    <div class="back-mark" aria-hidden="true"></div>
  </section>
</body>
</html>
```